Profesional personal website needs design and business card

I need a business card with my professional name as a logo "Marlo Vitality" for my business. I am a Wellness Coach, consultant and trainer. So it should be professional, wellness oriented and modern.

Target Market(s)

Private clients, governments, corporations. Luxury and high market.

Industry/Entity Type

Health And Wellness

Contact Information for Business Card

Marlo Vitality should be the logo

Colors

Designer to choose colors to be used in the design.

Requirements
Must have
• Marlo Vitality
• Name: Tomás Arribal
• Wellness Coach, Consultant & Trainer.
• Website: www.marlovitality.example
• Phone:
• Spain (+34) 612 480 397
• (USA) +1 (555) 318 2046
Nice to have
• The most important is the design of "Marlo Vitality", as this is going to be my personal brand logo. It should be professional, wellness, high end and actual.
Should not have
• no golds, no baroque style..

```html
<!DOCTYPE html>
<html lang="en">
<head>
<meta charset="utf-8">
<title>Marlo Vitality — Business Card</title>
<link rel="stylesheet" href="https://fonts.googleapis.com/css2?family=Cinzel:wght@600;700&family=Arimo:wght@400&display=swap">
<style>
  :root {
    --bg: #4a4a4a;
    --card-white: #ffffff;
    --green-deep: #0d6e35;
    --green-mid: #3f9a3f;
    --green-light: #7cc242;
    --green-title: #8cc63f;
    --text-grey: #555b5f;
    --serif: "Cinzel", "Trajan Pro", Georgia, serif;
    --sans: "Arimo", Arial, Helvetica, sans-serif;
  }
  * { box-sizing: border-box; margin: 0; padding: 0; }
  html, body { width: 1200px; height: 1200px; overflow: hidden; }
  body {
    background: var(--bg);
    display: flex;
    flex-direction: column;
    align-items: center;
    justify-content: center;
    gap: 60px;
  }
  .card {
    position: relative;
    width: 900px;
    height: 514px;
    border-radius: 26px;
    overflow: hidden;
    box-shadow: 0 10px 30px rgba(0,0,0,0.35);
  }

  /* Back */
  .card-back {
    background: linear-gradient(100deg, var(--green-deep) 0%, var(--green-mid) 50%, var(--green-light) 100%);
  }
  .card-back .pattern-field {
    position: absolute; inset: 0;
    background: linear-gradient(100deg, rgba(255,255,255,0.04), rgba(255,255,255,0.08));
  }
  .card-back .back-mark {
    position: absolute;
    right: 52px; bottom: 50px;
    display: flex; align-items: center; gap: 12px;
  }
  .back-mark .mark-circle {
    width: 26px; height: 26px; border-radius: 50%;
    border: 3px solid #fff;
  }
  .back-mark .mark-name {
    font-family: var(--serif);
    font-weight: 700;
    font-size: 22px;
    color: #fff;
    letter-spacing: 1px;
  }

  /* Front */
  .card-front { background: var(--card-white); }
  .brand-name {
    position: absolute; left: 58px; top: 58px;
    font-family: var(--serif); font-weight: 700;
    font-size: 40px; color: var(--green-deep);
    letter-spacing: 1px;
  }
  .person-name {
    position: absolute; left: 76px; top: 158px;
    font-family: var(--serif); font-weight: 700;
    font-size: 30px; color: var(--green-deep);
  }
  .person-title {
    position: absolute; left: 76px; top: 200px;
    font-family: var(--sans); font-size: 19px;
    color: var(--green-title);
  }
  .contact-list {
    position: absolute; left: 60px; top: 258px;
    list-style: none;
    font-family: var(--sans); font-size: 19px;
    color: var(--text-grey);
  }
  .contact-list li {
    display: flex; align-items: center; gap: 10px;
    height: 30px;
  }
  .contact-list svg { width: 16px; height: 16px; fill: var(--green-deep); flex: none; }

  .front-mark {
    position: absolute; left: 500px; top: 70px;
    width: 370px; height: 370px;
    border-radius: 50%;
    border: 10px solid var(--green-mid);
    display: flex; align-items: center; justify-content: center;
    text-align: center;
  }
  .front-mark .mark-name {
    font-family: var(--serif); font-weight: 700;
    font-size: 40px; line-height: 1.2;
    color: var(--green-deep);
  }
</style>
</head>
<body>

  <section class="card card-back">
    <div class="pattern-field" role="img" aria-label="Soft repeating brand pattern across the green card back"></div>
    <div class="back-mark">
      <span class="mark-circle"></span>
      <span class="mark-name">Marlo Vitality</span>
    </div>
  </section>

  <section class="card card-front">
    <h1 class="brand-name">Marlo Vitality</h1>
    <h2 class="person-name">Tomás Arribal</h2>
    <p class="person-title">Wellness Coach, Consultant &amp; Trainer</p>
    <ul class="contact-list">
      <li>
        <svg viewBox="0 0 24 24" aria-hidden="true"><path d="M6.6 10.8a15.1 15.1 0 0 0 6.6 6.6l2.2-2.2a1 1 0 0 1 1-.25 11.4 11.4 0 0 0 3.6.57 1 1 0 0 1 1 1V20a1 1 0 0 1-1 1A17 17 0 0 1 3 4a1 1 0 0 1 1-1h3.5a1 1 0 0 1 1 1c0 1.25.2 2.45.57 3.57a1 1 0 0 1-.25 1z"/></svg>
        Spain (+34) 612 480 397
      </li>
      <li>
        <svg viewBox="0 0 24 24" aria-hidden="true"><path d="M6.6 10.8a15.1 15.1 0 0 0 6.6 6.6l2.2-2.2a1 1 0 0 1 1-.25 11.4 11.4 0 0 0 3.6.57 1 1 0 0 1 1 1V20a1 1 0 0 1-1 1A17 17 0 0 1 3 4a1 1 0 0 1 1-1h3.5a1 1 0 0 1 1 1c0 1.25.2 2.45.57 3.57a1 1 0 0 1-.25 1z"/></svg>
        (USA) +1 (555) 318 2046
      </li>
      <li>
        <svg viewBox="0 0 24 24" aria-hidden="true"><path d="M12 2a10 10 0 1 0 0 20 10 10 0 0 0 0-20zm6.9 6h-2.9a15.7 15.7 0 0 0-1.4-3.6A8 8 0 0 1 18.9 8zM12 4c.8 1.2 1.5 2.5 1.9 4h-3.8c.4-1.5 1.1-2.8 1.9-4zM4.3 14a8.2 8.2 0 0 1 0-4h3.4a16.5 16.5 0 0 0 0 4zm.8 2h2.9c.3 1.3.8 2.5 1.4 3.6A8 8 0 0 1 5.1 16zM8 8H5.1a8 8 0 0 1 4.3-3.6C8.8 5.5 8.3 6.7 8 8zm4 12c-.8-1.2-1.5-2.5-1.9-4h3.8c-.4 1.5-1.1 2.8-1.9 4zm2.3-6H9.7a14.7 14.7 0 0 1 0-4h4.6a14.7 14.7 0 0 1 0 4zm.3 5.6c.6-1.1 1.1-2.3 1.4-3.6h2.9a8 8 0 0 1-4.3 3.6zM16.3 14a16.5 16.5 0 0 0 0-4h3.4a8.2 8.2 0 0 1 0 4z"/></svg>
        www.marlovitality.example
      </li>
    </ul>
    <div class="front-mark">
      <span class="mark-name">Marlo<br>Vitality</span>
    </div>
  </section>

</body>
</html>
```